Author book covers needed for a spiritual book, eastern wisdom

I need a cover for a 'Anthology'. I'm an author and I have established myself in a genre of its own, a symbiosis between spirituality and literature. My books are always a mix of entertainment and depth. Many of my readers have highlighted in the now eight books I have written many passages and asked me if it was not possible to collect all the wisdom, quotes, sayings and stories in a volume of aphorisms. I did this. Worker Title: "Lantern of quiet rain ... to let your days find their way home" Seeking a cover that this gold dust elements and at the same time combines the possibility of transformation and a bit mystical. .. Mainly it's in my books to eastern philosophies, ie Buddhism, Upanishads, the Vedas ... the Yoga Vasishta, the Bhagavad Gita and the like A variable template I found at plimvoro - but it is not a must, if anyone has a better has idea. Be creative! My author name: Marela Tovanni greetings Marela Tovanni

Target Market(s)

People who are spiritually interested and concerned about their lives make the book to be traded as a gift - and thus look accordingly.

Requirements
Must have
• a spiritual touch - spiritual touch if possible - a gift-character, so did customers feel inspired to give the book as a present to friends and relatives or other people. Please place the author's name at the lower end.
Nice to have
• Gold particles and Luminiscence ... to express did the word inside the book hopefully lighten up ones heart, to illumine ones soul or to help through a critical situation. So to say, bring some gold into a dark world ...
Should not have
• pls no black cover

```html
<!DOCTYPE html>
<html lang="en">
<head>
<meta charset="utf-8">
<title>Lantern of Quiet Rain – Cover</title>
<link href="https://fonts.googleapis.com/css2?family=Oswald:wght@500;700&family=Playfair+Display:ital@1&display=swap" rel="stylesheet">
<style>
  :root {
    --page-bg: #ffffff;
    --ink: #141210;
    --gold: #bf8a2a;
    --gold-deep: #8a5d14;
    --gold-bright: #d9a93c;
    --moss: #5d4a1c;
    --sand-light: #eadccb;
    --sand: #dcc7b0;
    --sand-warm: #d2b89c;
  }
  html, body {
    margin: 0;
    width: 1200px;
    height: 1200px;
    overflow: hidden;
    background: var(--page-bg);
  }
  .canvas {
    position: relative;
    width: 1200px;
    height: 1200px;
  }
  .cover {
    position: absolute;
    left: 250px;
    top: 70px;
    width: 700px;
    height: 1060px;
    overflow: hidden;
    box-shadow: 0 6px 24px rgba(0,0,0,0.18);
  }
  .cover-photo {
    position: absolute;
    inset: 0;
    background:
      radial-gradient(ellipse 60% 18% at 65% 22%, rgba(255,214,120,0.55), transparent 70%),
      linear-gradient(180deg,
        var(--gold-deep) 0%,
        var(--gold) 14%,
        #a57a2a 26%,
        var(--moss) 34%,
        #9c8468 37%,
        var(--sand-warm) 41%,
        var(--sand) 60%,
        var(--sand-light) 78%,
        var(--sand) 100%);
  }
  .heart-mark {
    position: absolute;
    left: 158px;
    top: 440px;
    width: 80px;
    height: 66px;
    border-radius: 40%;
    background: radial-gradient(circle, rgba(191,138,42,0.55), rgba(191,138,42,0) 70%);
  }
  .title {
    position: absolute;
    left: 0;
    right: 0;
    top: 500px;
    margin: 0;
    text-align: center;
    font-family: "Oswald", sans-serif;
    font-weight: 700;
    font-size: 84px;
    line-height: 1;
    letter-spacing: -1px;
    text-transform: uppercase;
    color: var(--ink);
  }
  .title .accent { color: var(--gold); }
  .subtitle {
    position: absolute;
    left: 0;
    right: 0;
    top: 620px;
    margin: 0;
    text-align: center;
    font-family: "Playfair Display", serif;
    font-style: italic;
    font-size: 30px;
    line-height: 1.2;
    color: var(--ink);
  }
  .author {
    position: absolute;
    left: 0;
    right: 0;
    top: 890px;
    margin: 0;
    text-align: center;
    font-family: "Oswald", sans-serif;
    font-weight: 500;
    font-size: 52px;
    letter-spacing: 14px;
    text-transform: uppercase;
    color: var(--gold);
  }
</style>
</head>
<body>
  <main class="canvas">
    <section class="cover">
      <div class="cover-photo" role="img" aria-label="Photograph of a small pale butterfly resting on a stone ledge, golden bokeh and glittering gold dust above, warm sandy stone below"></div>
      <div class="heart-mark" role="img" aria-label="Small dotted gold heart ornament"></div>
      <h1 class="title">Lantern<span class="accent">Quiet</span>Rain</h1>
      <p class="subtitle">to let your days find<br>their way home</p>
      <p class="author">Marela Tovanni</p>
    </section>
  </main>
</body>
</html>
```